Investment Firm Needs a Business Card Design

Need a business card for a new professional services firm that provides financial planning and investment management. Design should communicate financial safety and innovation. The contact information that needs to be on card is under Must Haves.

Target Market(s)

Retail Public

Industry/Entity Type

Investment

Requirements
Must have
• The data that needs to appear is in quotations:
"Daniel Hoskett, RWA"
(RWA logo either below my name or near my name)

"4417 Brambleton Lane
Suite 306
St. Charles, IL 60392"

"800-555-0143" (office)
"630-555-0187" (cell)
"dan@ledgerwisely.example" (email)
"www.LedgerWisely.example"
Nice to have
• would like to have the tag line "Steady Horizon(r)" with registered trade mark somewhere on card, maybe on back.

```html
<!DOCTYPE html>
<html lang="en">
<head>
<meta charset="utf-8">
<title>Ledger Wisely – Business Card</title>
<link rel="stylesheet" href="https://fonts.googleapis.com/css2?family=Spectral+SC:wght@700&family=Noto+Sans:wght@400&family=Roboto+Condensed:wght@700&display=swap">
<style>
  :root {
    --navy: #24297a;
    --green: #27a33a;
    --card: #ffffff;
    --backdrop: #e6e6e6;
    --text: #24297a;
  }
  * { margin: 0; padding: 0; box-sizing: border-box; }
  html, body {
    width: 1192px; height: 1200px; overflow: hidden;
    background: var(--backdrop);
  }
  .card {
    position: absolute; left: 180px; width: 832px;
    background: var(--card);
    box-shadow: 0 1px 3px rgba(0,0,0,.25);
    color: var(--text);
    font-family: "Noto Sans", sans-serif;
  }
  .card-front { top: 68px; height: 512px; }
  .card-back { top: 620px; height: 511px; }
  .stripe-navy { position: absolute; left: 0; top: 0; bottom: 0; width: 50px; background: var(--navy); }
  .stripe-green { position: absolute; left: 54px; top: 0; bottom: 0; width: 7px; background: var(--green); }
  .abs { position: absolute; white-space: nowrap; }

  .brand { display: flex; align-items: center; }
  .brand-square { background: var(--navy); }
  .brand-name {
    font-family: "Spectral SC", serif; font-weight: 700; color: var(--navy);
    letter-spacing: .5px; line-height: 1;
  }
  .front-brand { left: 90px; top: 44px; gap: 44px; }
  .front-brand .brand-square { width: 114px; height: 114px; }
  .front-brand .brand-name { font-size: 42px; }

  .rule-green { position: absolute; height: 1.5px; background: var(--green); }
  .front-rule { left: 90px; top: 165px; width: 541px; }
  .services { left: 90px; top: 173px; font-size: 22.5px; line-height: 30px; }

  .person-name {
    left: 89px; top: 293px; font-family: "Spectral SC", serif; font-weight: 700;
    font-size: 28px; line-height: 36px; color: var(--navy);
  }
  .credential { left: 87px; top: 342px; display: flex; align-items: center; gap: 8px; }
  .credential-badge { width: 50px; height: 30px; background: var(--navy); border-radius: 25px 25px 4px 4px; }
  .credential-title { font-family: "Roboto Condensed", sans-serif; font-weight: 700; font-size: 15px; }

  .contact { display: flex; align-items: center; gap: 10px; font-size: 19.5px; line-height: 28px; }
  .contact svg { width: 17px; height: 20px; flex: none; }
  .contact-cell { left: 470px; top: 296px; }
  .contact-office { left: 470px; top: 325px; }
  .contact-email { left: 470px; top: 354px; }
  .contact-web { left: 89px; top: 448px; }
  .address { left: 470px; top: 420px; display: flex; gap: 10px; font-size: 19.5px; line-height: 29px; }
  .address svg { width: 17px; height: 26px; margin-top: 2px; flex: none; }

  .back-brand { left: 206px; top: 160px; gap: 48px; }
  .back-brand .brand-square { width: 86px; height: 86px; }
  .back-brand .brand-name { font-size: 35px; }
  .back-rule { left: 194px; top: 292px; width: 494px; height: 1.5px; background: var(--navy); position: absolute; }
  .tagline { left: 0; right: 0; top: 312px; text-align: center; font-size: 30px; letter-spacing: .5px; }
  .tagline sup { font-size: 18px; vertical-align: 14px; }

  .features { top: 439px; display: flex; align-items: center; gap: 8px; font-size: 19.5px; }
  .features svg { width: 22px; height: 22px; }
  .f1 { left: 102px; } .f2 { left: 237px; } .f3 { left: 362px; } .f4 { left: 575px; }
</style>
</head>
<body>

<svg width="0" height="0" style="position:absolute">
  <defs>
    <symbol id="icon-tick" viewBox="0 0 22 22">
      <rect x="1.5" y="3.5" width="17" height="17" fill="none" stroke="#24297a" stroke-width="1.6"/>
      <path d="M4.5 11.5 L9 16.5 L20.5 2.5" fill="none" stroke="#27a33a" stroke-width="3.2" stroke-linejoin="round"/>
    </symbol>
  </defs>
</svg>

<section class="card card-front">
  <div class="stripe-navy"></div>
  <div class="stripe-green"></div>

  <div class="abs brand front-brand">
    <div class="brand-square"></div>
    <div class="brand-name">Ledger Wisely</div>
  </div>
  <div class="rule-green front-rule"></div>
  <div class="abs services">Retirement Planning / Investment Management</div>

  <div class="abs person-name">Daniel Hoskett</div>
  <div class="abs credential">
    <div class="credential-badge"></div>
    <span class="credential-title">Registered Wealth Advisor ™</span>
  </div>

  <div class="abs contact contact-cell">
    <svg viewBox="0 0 17 20"><rect x="3.5" y="1.5" width="10" height="17" rx="1.5" fill="none" stroke="#24297a" stroke-width="1.6"/><line x1="7" y1="15.5" x2="10" y2="15.5" stroke="#24297a" stroke-width="1.4"/></svg>
    <span>630-555-0187</span>
  </div>
  <div class="abs contact contact-office">
    <svg viewBox="0 0 17 20"><path d="M1 8 Q8.5 2 16 8 L14 10 L11.5 8.5 L11.5 7 Q8.5 6 5.5 7 L5.5 8.5 L3 10 Z" fill="#24297a"/><path d="M4 11 L13 11 L14.5 17 L2.5 17 Z" fill="#24297a"/><circle cx="8.5" cy="14" r="1.6" fill="#fff"/></svg>
    <span>800-555-0143</span>
  </div>
  <div class="abs contact contact-email">
    <svg viewBox="0 0 17 20"><rect x="1" y="5" width="15" height="10.5" fill="none" stroke="#24297a" stroke-width="1.6"/><path d="M1 5 L8.5 11 L16 5 M1 15.5 L6.5 10 M16 15.5 L10.5 10" fill="none" stroke="#24297a" stroke-width="1.4"/></svg>
    <span>dan@ledgerwisely.example</span>
  </div>
  <div class="abs address">
    <svg viewBox="0 0 17 26"><path d="M8.5 1 C4 1 1.5 4.3 1.5 8 C1.5 13 8.5 24 8.5 24 C8.5 24 15.5 13 15.5 8 C15.5 4.3 13 1 8.5 1 Z" fill="#24297a"/><circle cx="8.5" cy="8" r="2.6" fill="#fff"/></svg>
    <div>4417 Brambleton Lane, Suite 306<br>St. Charles, IL 60392</div>
  </div>
  <div class="abs contact contact-web">
    <svg viewBox="0 0 17 20"><circle cx="8.5" cy="10" r="7" fill="none" stroke="#24297a" stroke-width="1.3"/><ellipse cx="8.5" cy="10" rx="3" ry="7" fill="none" stroke="#24297a" stroke-width="1.1"/><path d="M1.5 10 H15.5 M2.8 6 H14.2 M2.8 14 H14.2" stroke="#24297a" stroke-width="1.1"/></svg>
    <span>www.LedgerWisely.example</span>
  </div>
</section>

<section class="card card-back">
  <div class="stripe-navy"></div>
  <div class="stripe-green"></div>

  <div class="abs brand back-brand">
    <div class="brand-square"></div>
    <div class="brand-name">Ledger Wisely</div>
  </div>
  <div class="back-rule"></div>
  <div class="abs tagline">Steady Horizon<sup>®</sup></div>

  <div class="abs features f1"><svg><use href="#icon-tick"/></svg><span>Fiduciary</span></div>
  <div class="abs features f2"><svg><use href="#icon-tick"/></svg><span>Flat-Fee</span></div>
  <div class="abs features f3"><svg><use href="#icon-tick"/></svg><span>Index Funds/ETFs</span></div>
  <div class="abs features f4"><svg><use href="#icon-tick"/></svg><span>Strategic Allocation</span></div>
</section>

</body>
</html>
```